Wake Me Up Sooner Landing Page and User Experience

We need a landing page design that we can use to mimic for our digital ads, social posts for our "Wake Me Up Sooner" campaign. We purchased the domain wakemeupsooner.example so there should be a heavy focus on that message. Wake Me Up Sooner should be playful and relate to the provocativeness and minor sexual innuendo of the statement but also tie into the real message which is to turn your air conditioning system on before summer comes to test and make sure it works. This way everyone isn't turning on their A/C at the same time on the first hot day of summer which results in overcrowding our air conditioning repair department. Our colors are black and yellow and the logo is attached.

Target Market(s)

Homeowners

Industry/Entity Type

Air Conditioning

Coding

Coded - Design and coding required

Number of Pages Required

1 page

Font styles to use
Other font styles liked:
• Times New Roman

Requirements
Must have
• -Logo
• -Submission form with first name, last name, email, phone, city, state that submits through this form URL: http://info.brambleworth.example/formhub/form/73204/8c2a:k-0007/1/-/-/-/-/index.htm (I can also provide the html for the form if it's easier)
• -clickable phone number in header 1-800-555-0187
• -address in footer Ashcombe, MA 01999
• -Responsive design to fit desktop/tablet/mobile
• -the following instructions: Simply follow these steps to make sure your unit is working:
• 1. Start your AC unit to "cool/on" position
• 2. Set the temperature at lowest setting
• 3. Listen for the Air Conditioning system to turn on
• 4. Feel for cold and freshness
• 5. If the system turns put on cool pair of shades and do a celebration dance
• 6. If the system does not turn on or is not blowing cool air contact us, Brambleworth is offering $50 Off Any Air Conditioning System Repair!
Nice to have
• Maybe an interactive message that instructs the customer to go test their air conditioner and then has them click whether it worked or not. If yes, display an image showing a celebratory depiction of being "cool". If no have the form appear to schedule our technician and assure them not to sweat, they'll be cool in no time.
• Maybe also offer to send a reminder to the customer if they are at work and not able to walk over to the thermostat
Should not have
• do not focus on other services: heating, plumbing, electrical etc...
• do not feature pictures of families, commercial projects, or air conditioner units

```html
<!DOCTYPE html>
<html lang="en">
<head>
<meta charset="utf-8">
<title>Wake Me Up Sooner | Brambleworth</title>
<link rel="stylesheet" href="https://fonts.googleapis.com/css2?family=Montserrat:wght@300;400;500;700;800;900&family=Great+Vibes&display=swap">
<style>
  :root {
    --black: #000000;
    --yellow: #ffeb00;
    --hero-top: #ffff00;
    --hero-mid: #ffc300;
    --hero-edge: #ff9a00;
    --green: #35b60a;
    --white: #ffffff;
    --ink: #0b0b0b;
    --pink: #ec6fb0;
    --violet: #a88acb;
    --blue: #0aaaee;
    --blue-text: #12a6e6;
  }
  * { box-sizing: border-box; margin: 0; padding: 0; }
  html, body { width: 976px; height: 1200px; overflow: hidden; }
  body { font-family: "Montserrat", sans-serif; color: var(--ink); position: relative; background: var(--black); }

  .site-header { position: absolute; left: 0; top: 0; width: 976px; height: 51px; background: var(--black); }
  .brand { position: absolute; left: 56px; top: 8px; height: 40px; display: flex; align-items: center; gap: 7px; color: var(--yellow); font-weight: 800; font-size: 22px; letter-spacing: 0.2px; text-decoration: none; }
  .brand-mark { width: 12px; height: 12px; background: var(--yellow); }
  .header-phone { position: absolute; right: 54px; top: 12px; display: flex; align-items: center; gap: 5px; color: var(--white); font-weight: 700; font-size: 21px; text-decoration: none; }
  .header-phone svg { width: 15px; height: 15px; }

  .hero { position: absolute; left: 0; top: 51px; width: 976px; height: 498px;
    background: radial-gradient(ellipse 70% 80% at 50% 0%, var(--hero-top) 0%, var(--hero-mid) 45%, var(--hero-edge) 100%); }
  .headline { position: absolute; left: 78px; top: 40px; font-weight: 900; color: var(--black); font-size: 112px; line-height: 116px; letter-spacing: 1px; }
  .headline-script { position: absolute; left: 60px; top: 240px; font-family: "Great Vibes", cursive; color: var(--white); font-size: 168px; line-height: 1; transform: rotate(-6deg); text-shadow: 14px 18px 18px rgba(230, 80, 0, 0.45); }
  .hero-lead { position: absolute; left: 81px; top: 443px; width: 380px; font-size: 15px; line-height: 18.5px; color: var(--ink); }

  .self-check { position: absolute; left: 666px; top: 44px; width: 256px; }
  .tab-active { position: absolute; left: 0; top: 0; width: 150px; height: 36px; background: var(--green); color: var(--white); font-weight: 700; font-size: 17px; padding: 10px 0 0 11px; }
  .tab-idle { position: absolute; left: 151px; top: 6px; width: 100px; height: 25px; background: var(--white); font-size: 12px; font-weight: 500; padding: 6px 0 0 13px; }
  .check-body { position: absolute; left: 0; top: 32px; width: 256px; height: 330px; background: var(--green); box-shadow: 0 8px 14px rgba(140, 70, 0, 0.35); text-align: center; color: var(--white); }
  .check-icon { width: 84px; height: 86px; margin: 40px auto 0; border-radius: 8px; background: rgba(255,255,255,0.25); }
  .check-text { margin: 23px auto 0; width: 200px; font-size: 15px; line-height: 18.5px; }
  .btn { display: flex; align-items: center; justify-content: center; background: var(--white); border-radius: 3px; font-weight: 700; font-size: 15px; text-decoration: none; letter-spacing: 0.3px; }
  .check-body .btn { width: 180px; height: 48px; margin: 25px auto 0; color: var(--green); }
  .link-small { color: var(--white); font-size: 10px; text-decoration: none; letter-spacing: 0.2px; }
  .check-body .link-small { display: block; margin-top: 10px; }

  .steps-section { position: absolute; left: 0; top: 549px; width: 976px; height: 549px;
    background: linear-gradient(110deg, var(--pink) 0%, var(--violet) 35%, #6d96d6 65%, var(--blue) 100%); color: var(--white); }
  .steps-title { position: absolute; left: 184px; top: 40px; font-weight: 400; font-size: 20px; letter-spacing: 0.6px; }
  .steps-sub { position: absolute; left: 184px; top: 73px; font-size: 15px; font-weight: 400; }
  .thermostat { position: absolute; left: 183px; top: 128px; width: 159px; height: 265px; border-radius: 5px; background: linear-gradient(180deg, #f4f6fd, #e9edfb); box-shadow: 0 3px 8px rgba(60, 60, 140, 0.3); }
  .step-list { position: absolute; left: 437px; top: 124px; width: 390px; list-style: none; font-size: 15px; line-height: 18px; }
  .step-list li { margin-bottom: 26px; }
  .step-list li:nth-child(5), .step-list li:nth-child(6) { margin-bottom: 26px; }
  .step-list strong { font-weight: 800; }
  .steps-actions { position: absolute; left: 437px; top: 444px; display: flex; align-items: center; gap: 5px; }
  .steps-actions .btn { width: 180px; height: 48px; color: var(--blue-text); }

  .site-footer { position: absolute; left: 0; top: 1098px; width: 976px; height: 102px; background: var(--black); color: var(--white); text-align: center; font-size: 15px; padding-top: 42px; }
</style>
</head>
<body>
  <header class="site-header">
    <a class="brand" href="#"><span class="brand-mark"></span>Brambleworth</a>
    <a class="header-phone" href="tel:18005550187">
      <svg viewBox="0 0 24 24" fill="#ffffff"><path d="M6.6 10.8a15.1 15.1 0 0 0 6.6 6.6l2.2-2.2a1 1 0 0 1 1-.25 11.4 11.4 0 0 0 3.6.57 1 1 0 0 1 1 1V20a1 1 0 0 1-1 1A17 17 0 0 1 3 4a1 1 0 0 1 1-1h3.5a1 1 0 0 1 1 1c0 1.25.2 2.45.57 3.57a1 1 0 0 1-.25 1z"/></svg>
      1-800-555-0187
    </a>
  </header>

  <section class="hero">
    <h1 class="headline">WAKE<br>ME UP</h1>
    <div class="headline-script">Sooner</div>
    <p class="hero-lead">Turn on your air conditioning system before summer comes to test and make sure it works.</p>

    <div class="self-check">
      <div class="check-body">
        <div class="check-icon" role="img" aria-label="Icon of a wall air conditioner blowing cool air"></div>
        <p class="check-text">Perform a self-check on your air conditioning unit to ensure that it is ready for the summer heat.</p>
        <a class="btn" href="#">I’M READY!</a>
        <a class="link-small" href="#">NO, MY UNIT DOESN’T WORK</a>
      </div>
      <div class="tab-active">Self Check</div>
      <div class="tab-idle">No Sweat...</div>
    </div>
  </section>

  <section class="steps-section">
    <h2 class="steps-title">ENSURE THAT YOUR AC UNIT IS WORKING</h2>
    <p class="steps-sub">Follow these simple steps:</p>
    <div class="thermostat" role="img" aria-label="Illustration of a thermostat app screen set to cool at 26 degrees"></div>
    <ol class="step-list">
      <li>Start your AC unit to "cool/on" position</li>
      <li>Set the temperature at lowest setting</li>
      <li>Listen for the Air Conditioning system to turn on</li>
      <li>Feel for cold and freshness</li>
      <li>If the system turns put on cool pair of shades and do a celebration dance</li>
      <li>If the system does not turn on or is not blowing cool air contact us, <strong>Brambleworth is offering $50 Off Any Air Conditioning System Repair!</strong></li>
    </ol>
    <div class="steps-actions">
      <a class="btn" href="#">I’M READY!</a>
      <a class="link-small" href="#">NO, MY UNIT DOESN’T WORK</a>
    </div>
  </section>

  <footer class="site-footer">Ashcombe, MA 01999</footer>
</body>
</html>
```